Business Card for a Floral & Decorating Business

I would like to take my current logo and create a better business card. I am looking for elegance as I am a florist and event decorator. My logo has multiple colour options. I like colours like green, purple, pink and orange, I think I would like a white card, open to black back ground. I want it to feel elegant and romantic. I like metallic lettering that maybe is indented in the paper, I also like glossy paper. I have a full logo already as well as a badge. I have attached both in multiple colours.m
Updates

Need extra days to review

Target Market(s)

Weddings, special events, floral customers

Industry/Entity Type

Floral and decorating

Contact Information for Business Card

Phone number, email, instagram, facebook, title, name, logo

Font styles to use
Script

Requirements
Nice to have
• Elegant

```html
<!DOCTYPE html>
<html lang="en">
<head>
<meta charset="utf-8">
<title>Maren Ellison – Business Card</title>
<link rel="stylesheet" href="https://fonts.googleapis.com/css2?family=Great+Vibes&family=Raleway:wght@400;500&family=Yellowtail&display=block">
<style>
  :root {
    --stage: #d9dbda;
    --plum: #7a6490;
    --plum-soft: #b3a4c3;
    --paper: #ffffff;
    --ink-light: #ffffff;
  }
  * { margin: 0; padding: 0; box-sizing: border-box; }
  html, body { width: 1200px; height: 1200px; overflow: hidden; }
  body { background: var(--stage); position: relative; font-family: "Raleway", sans-serif; }

  .card {
    position: absolute;
    left: 280px;
    width: 640px;
    height: 366px;
    border-radius: 26px;
    overflow: hidden;
    box-shadow: 0 8px 20px rgba(0,0,0,0.18);
  }
  .card--front { top: 194px; background: var(--plum); }
  .card--back { top: 640px; background: var(--paper); }

  .front__floral {
    position: absolute; top: 0; right: 0;
    width: 304px; height: 100%;
    background: linear-gradient(90deg, var(--plum) 0%, var(--plum) 30%, var(--plum-soft) 62%, var(--paper) 100%);
  }

  .front__identity { position: absolute; left: 48px; top: 156px; color: var(--ink-light); }
  .front__name {
    font-family: "Yellowtail", "Kaushan Script", cursive;
    font-size: 46px; line-height: 1; font-weight: 400; letter-spacing: 1px;
  }
  .front__title { font-size: 17px; margin-top: 8px; letter-spacing: 0.2px; }

  .front__contacts { position: absolute; left: 48px; top: 250px; list-style: none; color: var(--ink-light); }
  .front__contacts li { display: flex; align-items: center; gap: 9px; font-size: 15px; height: 21px; }
  .front__contacts li.phone { font-size: 18px; height: 25px; }
  .front__contacts svg { width: 11px; height: 11px; fill: var(--ink-light); flex: none; }

  .back__brand {
    position: absolute; top: 178px; left: 0; width: 100%;
    text-align: center; color: var(--plum);
  }
  .back__name {
    font-family: "Great Vibes", cursive;
    font-size: 66px; line-height: 1; font-weight: 400;
  }
  .back__social {
    position: absolute; top: 306px; left: 0; width: 100%;
    text-align: center; font-size: 15px; color: var(--plum); letter-spacing: 0.5px;
  }
</style>
</head>
<body>
  <section class="card card--front">
    <div class="front__floral" role="img" aria-label="Line-drawn white floral bouquet over a large purple letter on a white band"></div>

    <div class="front__identity">
      <h1 class="front__name">Maren Ellison</h1>
      <p class="front__title">Floral Stylist</p>
    </div>

    <ul class="front__contacts">
      <li class="phone">
        <svg viewBox="0 0 24 24"><path d="M6.6 10.8a15 15 0 0 0 6.6 6.6l2.2-2.2a1 1 0 0 1 1-.25 11.4 11.4 0 0 0 3.6.57 1 1 0 0 1 1 1V20a1 1 0 0 1-1 1A17 17 0 0 1 3 4a1 1 0 0 1 1-1h3.5a1 1 0 0 1 1 1c0 1.25.2 2.45.57 3.57a1 1 0 0 1-.25 1z"/></svg>
        555.214.7720
      </li>
      <li>
        <svg viewBox="0 0 24 24"><path d="M2 5h20v14H2z M2 5l10 8 10-8" fill="none" stroke="#fff" stroke-width="2.5"/></svg>
        hello@marenellison.com
      </li>
      <li>
        <svg viewBox="0 0 24 24"><circle cx="12" cy="12" r="10"/></svg>
        marenellison.com
      </li>
    </ul>
  </section>

  <section class="card card--back">
    <div class="back__brand">
      <span class="back__name">Maren Ellison</span>
    </div>
    <p class="back__social">@marenellison</p>
  </section>
</body>
</html>
```